Marlow Creek sign

24"x36" sign for new home construction job site. Located in affluent in-town neighborhood in Midwest. Traditional american style homes. 2nd generation construction company. Sign needs to convey strength and elegance but not overly elaborate. Competition most has signs consisting of text.

Sign text reads:
Marlow Creek Builders
Custom Luxury for Over 20 years
248-555-0137

Target Market(s)

Upper middle income home buyers

Industry/Entity Type

Construction

Font styles to use
Serif
Decorative

Requirements
Must have
• Logo image no more than 2 colors
Nice to have
• Should be visible and legible from distance of 30'
Should not have
• Not just image of house as logo

```html
<!DOCTYPE html>
<html lang="en">
<head>
<meta charset="utf-8">
<title>Marlow Creek Builders – Job Site Sign</title>
<link rel="stylesheet" href="https://fonts.googleapis.com/css2?family=Cormorant+Garamond:wght@600&family=Libre+Caslon+Text:wght@700&family=Parisienne&display=swap">
<style>
  :root {
    --maroon: #7d1935;
    --silver: #a7a7a7;
    --paper: #ffffff;
  }
  html, body {
    margin: 0;
    padding: 0;
    width: 1200px;
    height: 800px;
    overflow: hidden;
    background: var(--paper);
  }
  .sign {
    display: block;
    width: 1200px;
    height: 800px;
  }
  .frame-outer { fill: none; stroke: var(--maroon); stroke-width: 3; }
  .frame-inner { fill: none; stroke: var(--maroon); stroke-width: 7; }
  .divider { stroke: var(--maroon); stroke-width: 5; }
  .tagline-band { fill: var(--silver); }
  .name-rule { fill: var(--silver); }
  .company-name {
    font-family: "Cormorant Garamond", "Times New Roman", serif;
    font-weight: 600;
    font-size: 132px;
    fill: var(--maroon);
  }
  .company-trade {
    font-family: "Libre Caslon Text", Georgia, serif;
    font-weight: 700;
    font-size: 128px;
    fill: var(--maroon);
  }
  .tagline {
    font-family: "Parisienne", cursive;
    font-size: 76px;
    fill: var(--paper);
  }
  .phone {
    font-family: "Libre Caslon Text", Georgia, serif;
    font-weight: 700;
    fill: var(--maroon);
  }
  .phone-area { font-size: 96px; }
  .phone-number { font-size: 160px; }
  .phone-dot { fill: var(--silver); }
</style>
</head>
<body>
<svg class="sign" viewBox="0 0 1200 800" xmlns="http://www.w3.org/2000/svg" aria-label="Marlow Creek Builders – Custom Luxury for Over 20 years – (248) 555-0137">
  <rect class="frame-outer" x="8" y="8" width="1184" height="784"/>
  <rect class="frame-inner" x="24" y="24" width="1152" height="752"/>

  <g class="name-block">
    <text class="company-name" x="96" y="178" textLength="1008" lengthAdjust="spacingAndGlyphs">MARLOW CREEK</text>
    <rect class="name-rule" x="96" y="210" width="1008" height="6"/>
    <text class="company-trade" x="96" y="340" textLength="1008" lengthAdjust="spacing">BUILDERS</text>
  </g>

  <line class="divider" x1="24" y1="424" x2="1176" y2="424"/>
  <rect class="tagline-band" x="24" y="432" width="1152" height="132"/>
  <line class="divider" x1="24" y1="572" x2="1176" y2="572"/>

  <text class="tagline" x="600" y="524" text-anchor="middle" textLength="990" lengthAdjust="spacingAndGlyphs">Custom Luxury for Over 20 years</text>

  <g class="phone">
    <text class="phone-area" x="200" y="700" textLength="210" lengthAdjust="spacingAndGlyphs">(248)</text>
    <text class="phone-number" x="430" y="714" textLength="220" lengthAdjust="spacingAndGlyphs">555</text>
    <circle class="phone-dot" cx="670" cy="664" r="11"/>
    <text class="phone-number" x="690" y="714" textLength="310" lengthAdjust="spacingAndGlyphs">0137</text>
  </g>
</svg>
</body>
</html>
```